Business Card Design Project

Recently had a new logo made up for my company and new business cards done as well. I have attached the logos for your viewing. Additional projects may be needed. Good luck!

Business

```html
<!DOCTYPE html>
<html lang="en">
<head>
<meta charset="utf-8">
<title>Marbrook Financial Group – Business Card</title>
<link rel="stylesheet" href="https://fonts.googleapis.com/css2?family=Bodoni+Moda:wght@400&display=swap">
<style>
  :root {
    --navy: #161a26;
    --gold: #cdc77e;
    --paper: #ffffff;
    --ink: #111111;
  }
  html, body {
    margin: 0;
    padding: 0;
    overflow: hidden;
    background: var(--paper);
  }
  .card {
    position: relative;
    width: 776px;
    height: 1200px;
    overflow: hidden;
    background: var(--paper);
    font-family: "Bodoni Moda", "Times New Roman", serif;
    color: var(--ink);
  }
  .header-band {
    position: absolute;
    left: 0; top: 0;
    width: 776px;
    height: 257px;
    background: var(--navy);
  }
  .brand {
    position: absolute;
    left: 70px;
    top: 78px;
    height: 111px;
    display: flex;
    align-items: center;
    gap: 22px;
  }
  .brand-square {
    width: 100px;
    height: 100px;
    box-sizing: border-box;
    border: 4px solid var(--gold);
  }
  .brand-name {
    color: var(--gold);
    font-weight: 400;
    font-size: 30px;
    letter-spacing: 3px;
    white-space: nowrap;
  }
  .identity {
    position: absolute;
    left: 0;
    width: 776px;
    top: 336px;
    text-align: center;
  }
  .person-name {
    margin: 0;
    font-weight: 400;
    font-size: 48px;
    line-height: 1;
  }
  .person-title {
    margin: 18px 0 0;
    font-size: 25px;
    line-height: 1;
  }
  .rule {
    position: absolute;
    left: 108px;
    top: 459px;
    width: 560px;
    height: 4px;
    background: var(--ink);
  }
  .contact, .address {
    position: absolute;
    left: 0;
    width: 776px;
    text-align: center;
    font-size: 35px;
    line-height: 44px;
    margin: 0;
  }
  .contact { top: 612px; }
  .address { top: 781px; line-height: 48px; }
  .contact span, .address span { display: block; }
  .wave {
    position: absolute;
    left: 0; top: 0;
  }
</style>
</head>
<body>
  <div class="card">
    <div class="header-band"></div>
    <div class="brand">
      <div class="brand-square"></div>
      <div class="brand-name">MARBROOK FINANCIAL GROUP</div>
    </div>

    <div class="identity">
      <h1 class="person-name">Daniel R. Marbrook</h1>
      <p class="person-title">Estate Planning &amp; Insurance Specialist</p>
    </div>
    <div class="rule"></div>

    <p class="contact">
      <span>P: 555-214-7380 F: 555-214-6091</span>
      <span>Dmarbrook@marbrookfinancial.com</span>
      <span>www.marbrookfinancial.com</span>
    </p>

    <p class="address">
      <span>4120 Linden Parkway, Suite 310E</span>
      <span>Brookvale, New York 11000</span>
    </p>

    <svg class="wave" width="776" height="1200" viewBox="0 0 776 1200" aria-hidden="true">
      <path fill="var(--gold)" d="M0,813 C110,870 160,975 230,1030 C400,1150 600,1125 776,1070 L776,1200 L0,1200 Z"/>
      <path fill="var(--navy)" d="M0,885 C120,925 180,990 230,1030 C400,1140 620,1145 776,1132 L776,1200 L0,1200 Z"/>
    </svg>
  </div>
</body>
</html>
```